Tail Haven Pet Services ABN 31 640 975 208 needs a Postcard Design

Genuine pet lover offering a professional and highly personalised pet service. I will visit your home daily to care for your pet in their own environment. THE OTHER OPTION FOR WHEN YOU GO ON HOLIDAYS. Dog Holiday Service (includes but not limited to) Feed, Water, Walk, Love & Play. Clean Litter Trays, Hutches & Cages. Administer Medication as Directed. Water Pot Plants & Collec Mail. Individual Dog Walking (Permanent or Casual). REASONABLE RATES. Police Check & References available upon request. Contact MARGOT 0412 846 293

```html
<!DOCTYPE html>
<html lang="en">
<head>
<meta charset="utf-8">
<title>Tail Haven Pet Services – Postcard</title>
<link rel="stylesheet" href="https://fonts.googleapis.com/css2?family=Roboto+Condensed:wght@700&family=Lato:wght@400&display=swap">
<style>
  :root {
    --page-bg: #e9eaec;
    --sky: #1fa8d6;
    --sky-light: #4fc7ec;
    --sky-deep: #0e8fc0;
    --ink: #1b1b1b;
    --white: #ffffff;
    --photo-light: #f1efea;
    --photo-mid: #d9d4cb;
    --line: #3a3a3a;
  }
  * { box-sizing: border-box; margin: 0; padding: 0; }
  html, body { width: 900px; height: 1200px; overflow: hidden; }
  body { background: var(--page-bg); position: relative; font-family: "Roboto Condensed", "Arial Narrow", sans-serif; }

  .postcard {
    position: absolute;
    left: 90px;
    width: 720px;
    height: 540px;
    background: var(--white);
    overflow: hidden;
    box-shadow: 0 6px 18px rgba(0,0,0,0.18);
  }
  .postcard--front { top: 40px; }
  .postcard--back { top: 620px; }
  .postcard svg.artwork { position: absolute; inset: 0; }

  .headline { position: absolute; left: 28px; text-transform: uppercase; font-weight: 700; line-height: 1; }
  .headline--lead { top: 50px; font-size: 40px; color: var(--white); }
  .headline--sub { top: 100px; font-size: 23px; color: var(--white); }
  .headline--dark { top: 134px; font-size: 29px; color: var(--ink); }
  .headline--big { top: 172px; font-size: 52px; color: var(--ink); }

  .service-title { position: absolute; left: 30px; top: 58px; font-size: 22px; color: var(--white); font-weight: 700; }
  .service-list { position: absolute; left: 28px; top: 94px; font-family: "Lato", Arial, sans-serif; font-size: 17.5px; line-height: 26px; color: var(--ink); list-style: none; }
  .service-list li:first-child { padding-left: 4px; }

  .extras-pill {
    position: absolute; left: 24px; top: 208px; width: 360px; height: 92px;
    background: var(--ink); border-radius: 46px;
    padding: 14px 0 0 30px;
    color: var(--white); font-size: 27px; line-height: 31px; font-weight: 700; text-transform: uppercase;
  }

  .promise { position: absolute; left: 28px; top: 334px; font-size: 27px; line-height: 31px; font-weight: 700; text-transform: uppercase; }
  .promise--light { color: var(--white); }
  .promise--dark { color: var(--ink); top: 427px; }
</style>
</head>
<body>

<section class="postcard postcard--front">
  <svg class="artwork" width="720" height="540" viewBox="0 0 720 540" xmlns="http://www.w3.org/2000/svg">
    <defs>
      <radialGradient id="sunburst" cx="0.22" cy="0.75" r="0.8">
        <stop offset="0" stop-color="var(--sky-light)"/>
        <stop offset="0.6" stop-color="var(--sky)"/>
        <stop offset="1" stop-color="var(--sky-deep)"/>
      </radialGradient>
      <linearGradient id="puppyPhoto" x1="0" y1="0" x2="0" y2="1">
        <stop offset="0" stop-color="var(--photo-mid)"/>
        <stop offset="0.6" stop-color="var(--photo-light)"/>
        <stop offset="1" stop-color="#ffffff"/>
      </linearGradient>
      <linearGradient id="pugPhoto" x1="0" y1="0" x2="0" y2="1">
        <stop offset="0" stop-color="#5a5650"/>
        <stop offset="1" stop-color="#c9b89c"/>
      </linearGradient>
    </defs>
    <rect class="front-bg" width="720" height="540" fill="url(#sunburst)"/>
    <path class="swoosh-black" transform="translate(-26 0)" d="M520 0 H760 V540 H540 C430 540 340 500 305 450 C292 430 298 410 310 392 Z" fill="var(--ink)"/>
    <path class="swoosh-white" transform="translate(-12 0)" d="M520 0 H760 V540 H540 C430 540 340 500 305 450 C292 430 298 410 310 392 Z" fill="var(--white)"/>
    <path class="puppy-photo" role="img" aria-label="Photo of a white puppy resting its head on its paws" d="M520 0 H760 V540 H540 C430 540 340 500 305 450 C292 430 298 410 310 392 Z" fill="url(#puppyPhoto)"/>
    <circle class="pug-frame" cx="155" cy="405" r="96" fill="var(--ink)"/>
    <circle class="pug-ring" cx="155" cy="405" r="90" fill="var(--white)"/>
    <circle class="pug-photo" role="img" aria-label="Photo of a pug sitting in a car seat" cx="155" cy="405" r="84" fill="url(#pugPhoto)"/>
  </svg>
  <h1 class="headline headline--lead">Genuine Pet Lover</h1>
  <p class="headline headline--sub">Offering a professional and</p>
  <p class="headline headline--dark">Highly personalised</p>
  <p class="headline headline--big">Pet Service</p>
</section>

<section class="postcard postcard--back">
  <svg class="artwork" width="720" height="540" viewBox="0 0 720 540" xmlns="http://www.w3.org/2000/svg">
    <defs>
      <linearGradient id="panelBlue" x1="0" y1="0" x2="1" y2="1">
        <stop offset="0" stop-color="var(--sky)"/>
        <stop offset="1" stop-color="var(--sky-light)"/>
      </linearGradient>
      <linearGradient id="papillonPhoto" x1="0" y1="0" x2="0" y2="1">
        <stop offset="0" stop-color="#3d7fd1"/>
        <stop offset="1" stop-color="#b8c6da"/>
      </linearGradient>
    </defs>
    <path class="panel-black" transform="translate(26 0)" d="M0 0 H300 L545 360 Q575 410 540 450 L430 540 H0 Z" fill="var(--ink)"/>
    <path class="panel-white" transform="translate(12 0)" d="M0 0 H300 L545 360 Q575 410 540 450 L430 540 H0 Z" fill="var(--white)"/>
    <path class="panel-blue" d="M0 0 H300 L545 360 Q575 410 540 450 L430 540 H0 Z" fill="url(#panelBlue)"/>
    <rect class="stamp-box" x="607" y="60" width="84" height="92" fill="none" stroke="var(--line)" stroke-width="1.2"/>
    <g class="address-lines" stroke="var(--line)" stroke-width="1.2">
      <line x1="512" y1="224" x2="690" y2="224"/>
      <line x1="512" y1="254" x2="690" y2="254"/>
      <line x1="512" y1="285" x2="690" y2="285"/>
    </g>
  </svg>
  <h2 class="service-title">DOG HOLIDAY SERVICE</h2>
  <ul class="service-list">
    <li>Feed, Water, Walk, Love &amp; Play.</li>
    <li>Clean Litter Trays, Hutches &amp; Cages.</li>
    <li>Administer Medication as Directed.</li>
  </ul>
  <p class="extras-pill">Water Pot Plants<br>&amp; Collec Mail</p>
  <svg class="artwork" width="720" height="540" viewBox="0 0 720 540" xmlns="http://www.w3.org/2000/svg">
    <circle class="papillon-frame" cx="413" cy="250" r="66" fill="var(--ink)"/>
    <circle class="papillon-ring" cx="413" cy="250" r="61" fill="var(--white)"/>
    <circle class="papillon-photo" role="img" aria-label="Photo of a small papillon dog beside a pet carrier" cx="413" cy="250" r="56" fill="url(#papillonPhoto)"/>
  </svg>
  <p class="promise promise--light">I will visit your home<br>daily to care for your pet<br>in their own environment.</p>
  <p class="promise promise--dark">The other option for when<br>you go on holidays.</p>
</section>

</body>
</html>
```